Flyer for Quarry Lumina - Design Agency

We need a 4-page square flyer measuring 14.8x14.8cm per page, to fold out, for a design agency targeting small businesses.
The design should be very modern. There shouldn't be too much content visible.
The background should be black. The color of the logo (attached) can also be used. The content is also attached and divided per page. We are open to alternative suggestions regarding the division.

```html
<!DOCTYPE html>
<html lang="de">
<head>
<meta charset="utf-8">
<title>Quarry Lumina – Faltflyer</title>
<link rel="stylesheet" href="https://fonts.googleapis.com/css2?family=Bebas+Neue&family=Oswald:wght@200;500;700&family=Poppins:wght@400;500;600;700&family=Allura&display=swap">
<style>
:root{
  --page:#e4e4e4;
  --black:#05070b;
  --navy:#0b1a2e;
  --blue:#2f7cf6;
  --blue-light:#4d8fff;
  --cyan:#5ff5ef;
  --teal:#19d4c4;
  --yellow:#ecf33a;
  --white:#ffffff;
  --text:#e8eef7;
}
*{box-sizing:border-box;margin:0;padding:0}
html,body{width:1200px;height:2212px;overflow:hidden;background:var(--page)}
body{position:relative;font-family:"Poppins",sans-serif;color:var(--text)}
.spread{position:absolute;left:0;width:1200px;height:600px;overflow:hidden;background:var(--black)}
.spread--outside{top:456px}
.spread--inside{top:1156px;background:linear-gradient(90deg,#0f2d55 0%,#0a1a30 40%,#06090f 62%,#05070b 100%)}
.abs{position:absolute;z-index:2}
.fill{position:absolute;border-radius:12px;z-index:1}
.center{text-align:center;left:0;width:600px}

/* outside: back panel */
.back-photo{left:0;top:0;width:600px;height:600px;border-radius:0;z-index:0;
  background:radial-gradient(ellipse at 40% 30%,#1b3550 0%,#0d1b2b 45%,#05080d 100%)}
.front-glow{left:600px;top:0;width:600px;height:600px;border-radius:0;z-index:0;
  background:radial-gradient(ellipse at 60% 75%,#123a5a 0%,#081521 45%,#05070b 80%)}
.brand{font-family:"Poppins",sans-serif;font-weight:600;color:var(--cyan);letter-spacing:.5px;white-space:nowrap}
.brand--back{top:90px;font-size:36px}
.script{font-family:"Allura",cursive;color:var(--yellow);white-space:nowrap}
.back-tagline{top:180px;font-size:38px}
.back-headline{top:218px;font-family:"Bebas Neue",sans-serif;font-size:38px;color:var(--blue-light);letter-spacing:.5px}
.owner-label{top:262px;font-size:13px;font-weight:700;letter-spacing:4px;color:#cdf9f6}
.owner-pill{left:182px;top:284px;width:230px;height:24px;border-radius:12px;
  background:linear-gradient(90deg,var(--cyan) 0 44%,var(--blue) 56% 100%);
  display:flex;align-items:center;justify-content:space-between;padding:0 10px;font-size:11px;font-weight:600}
.owner-pill .name-a{color:#06222a}
.owner-pill .name-b{color:var(--white)}
.owner-and{position:absolute;left:100px;top:-3px;width:30px;height:30px;border-radius:50%;
  background:var(--blue);border:3px solid #a8c8ff;color:#fff;font-size:13px;display:flex;align-items:center;justify-content:center}
.contact-lead{top:328px;font-size:17px;font-weight:700;color:var(--white)}
.contact-script{top:352px;font-size:32px;color:var(--white)}
.contact-list{top:404px;font-size:12px;color:var(--white);line-height:1.25}
.contact-item{display:flex;flex-direction:column;align-items:center;margin-bottom:5px}
.contact-item svg{margin-bottom:3px}

/* outside: front panel */
.brand--front{left:600px;width:600px;top:50px;font-size:40px;text-align:center}
.front-script{left:600px;width:600px;top:126px;font-size:60px;text-align:center}
.front-headline{position:absolute;z-index:3;left:600px;width:600px;top:192px;text-align:center;font-family:"Bebas Neue",sans-serif;
  font-size:86px;line-height:.76;font-weight:400;color:var(--teal);white-space:nowrap}
.front-headline span{display:block;background:linear-gradient(180deg,#6ffff6,#14c7b7);-webkit-background-clip:text;background-clip:text;color:transparent}

/* inside: left panel */
.claim{left:41px;top:30px;font-family:"Oswald",sans-serif;line-height:.98;font-size:62px;text-transform:uppercase;white-space:nowrap}
.claim .thin{font-weight:200;color:var(--cyan);display:block}
.claim .bold{font-weight:700;color:var(--cyan);display:block;font-size:60px}
.claim .accent{font-weight:700;color:var(--yellow);display:block;font-size:60px}
.intro{left:47px;top:232px;border-left:3px solid var(--white);padding-left:12px;font-size:17px;font-weight:700;color:var(--white);line-height:1.2;width:240px}
.idea-box{left:43px;top:349px;width:280px;height:200px;border-radius:12px;overflow:hidden;
  background:linear-gradient(90deg,var(--blue) 0%,#1f5fbf 60%,#0f2d55 100%)}
.idea-box .kicker{position:absolute;left:22px;top:22px;font-size:14px;font-weight:700;color:var(--white);white-space:nowrap}
.idea-box .title{position:absolute;left:22px;top:40px;font-family:"Bebas Neue",sans-serif;font-size:33px;line-height:1;color:var(--white);white-space:nowrap}
.idea-box .body{position:absolute;left:22px;top:82px;font-size:14px;line-height:1.12;color:var(--white);width:200px}
.idea-box .extra{position:absolute;left:0;bottom:0;width:100%;height:52px;background:linear-gradient(90deg,#2a6fe0,#163a70);
  padding:9px 22px;font-size:26px;font-weight:700;color:var(--yellow);white-space:nowrap}

/* inside: right panel */
.section-title{font-size:22px;font-weight:700;color:var(--yellow);white-space:nowrap}
.service-pill{height:26px;width:194px;border-radius:13px;font-size:15px;font-weight:600;display:flex;align-items:center;justify-content:center;white-space:nowrap}
.service-pill--blue{background:var(--blue);color:var(--white)}
.service-pill--cyan{background:var(--cyan);color:#06222a}
.service-text{font-size:13.5px;line-height:1.1;color:var(--white)}
.why-row{left:643px;top:423px;width:515px;height:139px;display:flex;border-radius:8px}
.why-card{flex:1;background:var(--blue);display:flex;flex-direction:column;align-items:center;text-align:center;padding:12px 6px 0;font-size:13px;line-height:1.1;color:var(--white)}
.why-card--mid{background:#3d8ef5;margin-top:-8px;padding-top:20px}
.why-card strong{color:var(--yellow);font-weight:600;display:block}
.why-card svg{margin-bottom:6px}
</style>
</head>
<body>

<!-- Outside spread: back panel + front cover -->
<section class="spread spread--outside" aria-label="Außenseite">
  <div class="fill back-photo" role="img" aria-label="Unscharfes, dunkelblaues Foto eines Serverraums"></div>
  <div class="fill front-glow"></div>

  <div class="abs center brand brand--back">Quarry Lumina</div>
  <div class="abs center script back-tagline">Designs, die wirken</div>
  <div class="abs center back-headline">MARKEN, DIE BLEIBEN</div>
  <div class="abs center owner-label">INHABER</div>
  <div class="abs owner-pill"><span class="name-a">Lio Brandt</span><span class="owner-and">&amp;</span><span class="name-b">Tessa Vahl</span></div>
  <div class="abs center contact-lead">Kontaktiere uns für eine</div>
  <div class="abs center script contact-script">kostenlose Beratung!</div>

  <div class="abs center contact-list">
    <div class="contact-item">
      <svg width="13" height="13" viewBox="0 0 14 14"><circle cx="7" cy="7" r="7" fill="#4d8fff"/><path d="M7 3a2.4 2.4 0 0 0-2.4 2.4C4.6 7.4 7 10.5 7 10.5s2.4-3.1 2.4-5.1A2.4 2.4 0 0 0 7 3z" fill="#fff"/></svg>
      <span>Ahornallee 12<br>60311 Frankfurt</span>
    </div>
    <div class="contact-item">
      <svg width="13" height="13" viewBox="0 0 14 14"><circle cx="7" cy="7" r="7" fill="#4d8fff"/><path d="M4.5 3.6l1.4-.3.8 1.8-.9.7a5 5 0 0 0 2.4 2.4l.7-.9 1.8.8-.3 1.4c-3.3.3-6.2-2.6-5.9-5.9z" fill="#fff"/></svg>
      <span>+49 000 11223</span>
    </div>
    <div class="contact-item">
      <svg width="13" height="13" viewBox="0 0 14 14"><circle cx="7" cy="7" r="7" fill="#4d8fff"/><rect x="3.5" y="4.5" width="7" height="5" rx=".8" fill="#fff"/><path d="M3.7 4.8L7 7.3l3.3-2.5" stroke="#4d8fff" stroke-width=".8" fill="none"/></svg>
      <span>hallo@quarrylumina.de</span>
    </div>
    <div class="contact-item">
      <svg width="13" height="13" viewBox="0 0 14 14"><circle cx="7" cy="7" r="7" fill="#4d8fff"/><circle cx="7" cy="7" r="3.4" fill="none" stroke="#fff" stroke-width=".9"/><path d="M3.6 7h6.8M7 3.6c-1.6 2-1.6 4.8 0 6.8M7 3.6c1.6 2 1.6 4.8 0 6.8" stroke="#fff" stroke-width=".7" fill="none"/></svg>
      <span>www.quarrylumina.de</span>
    </div>
  </div>

  <div class="fill" role="img" aria-label="3D-Icon: blaue Ausrichtungs-Kachel" style="left:118px;top:444px;width:82px;height:66px;background:linear-gradient(135deg,#5aa0ff,#2a63d8);transform:rotate(-20deg)"></div>
  <div class="fill" role="img" aria-label="3D-Icon: orange Smartphone-Kachel mit Zeichenwerkzeugen" style="left:430px;top:240px;width:58px;height:90px;background:linear-gradient(135deg,#ffb347,#f07b12);transform:rotate(20deg)"></div>
  <div class="fill" role="img" aria-label="3D-Icon: Farbkarte" style="left:410px;top:522px;width:68px;height:44px;background:linear-gradient(180deg,#f4f6fb,#c9d2e6);transform:rotate(8deg)"></div>

  <div class="abs brand brand--front">Quarry Lumina</div>
  <div class="abs script front-script">Dein Unternehmen</div>
  <h1 class="front-headline"><span>DEIN STIL</span><span>UNSER DESIGN</span></h1>

  <div class="fill" role="img" aria-label="Person von hinten am Bildschirm mit Design-Schriftzug" style="left:772px;top:352px;width:240px;height:248px;border-radius:14px 14px 0 0;background:linear-gradient(180deg,#2a3340 0%,#3e5f8d 55%,#1d3a62 100%)"></div>
  <div class="fill" role="img" aria-label="Schwebende Werkzeugleiste mit Design-Icons" style="left:630px;top:290px;width:90px;height:300px;background:linear-gradient(180deg,#1b2c44,#0c1726);transform:rotate(-14deg)"></div>
  <div class="fill" role="img" aria-label="3D-Glühbirne" style="left:650px;top:196px;width:50px;height:60px;border-radius:50%;background:radial-gradient(circle,#ffcf7a,#c7782a)"></div>
  <div class="fill" role="img" aria-label="3D-Icon: lila Stift-Kachel" style="left:728px;top:370px;width:58px;height:58px;background:linear-gradient(135deg,#7c6cff,#4a3bd6);transform:rotate(-14deg)"></div>
  <div class="fill" role="img" aria-label="3D-Icon: Text-Kachel" style="left:1082px;top:330px;width:50px;height:50px;background:linear-gradient(135deg,#d34cff,#8b1fd0);transform:rotate(8deg)"></div>
  <div class="fill" role="img" aria-label="Panel mit Formwerkzeugen und Farbfächer" style="left:1040px;top:390px;width:128px;height:150px;background:linear-gradient(160deg,#1a2b42,#0e1a29);transform:rotate(14deg)"></div>
  <div class="fill" role="img" aria-label="Farbfächer" style="left:1030px;top:480px;width:84px;height:60px;background:linear-gradient(120deg,#f3e2c8,#d66b8a,#6a3fa0);transform:rotate(-20deg)"></div>
  <div class="fill" role="img" aria-label="3D-Icon: Farbkreis-Kachel" style="left:1110px;top:200px;width:62px;height:62px;background:linear-gradient(135deg,#16324e,#0b1b2d);transform:rotate(10deg)"></div>
  <div class="fill" role="img" aria-label="3D-Icon: rosa Ordner-Kachel" style="left:680px;top:540px;width:58px;height:52px;background:linear-gradient(135deg,#ff9dd6,#ec5bb5);transform:rotate(-14deg)"></div>
  <div class="fill" role="img" aria-label="Vektor-Pfad mit Ankerpunkten" style="left:1110px;top:86px;width:60px;height:36px;background:linear-gradient(135deg,#3a2a1e,#1a1410)"></div>
</section>

<!-- Inside spread -->
<section class="spread spread--inside" aria-label="Innenseite">
  <h2 class="abs claim"><span class="thin">Modern,</span><span class="bold">Mutig,</span><span class="accent">Markant</span></h2>
  <p class="abs intro">Quarry Lumina gestaltet die Zukunft deines Unternehmensauftritts.</p>

  <div class="abs idea-box">
    <div class="kicker">WIR MACHEN AUS IDEEN</div>
    <div class="title">VISUELLE ERLEBNISSE</div>
    <div class="body">und sorgen dafür, dass deine Marke im Gedächtnis bleibt.</div>
    <div class="extra">+ Grafiken</div>
  </div>

  <div class="fill" role="img" aria-label="3D-Laptop mit schwebenden Design-Icons, Papierflieger und Zahnrad" style="left:334px;top:70px;width:224px;height:490px;background:linear-gradient(180deg,#1c3c6b 0%,#3a4f8f 45%,#b7b9e8 80%,#8f93d6 100%);opacity:.9"></div>

  <div class="abs section-title" style="left:652px;top:40px">Unsere Leistungen</div>

  <svg class="abs" style="left:620px;top:40px" width="560" height="380" viewBox="0 0 560 380" aria-hidden="true">
    <g fill="none" stroke="#ffffff" stroke-width="1.6" stroke-dasharray="2 4" stroke-linecap="round">
      <path d="M252 26c50-6 90 8 100 40"/>
      <path d="M56 62C10 90 -4 150 36 190"/>
      <path d="M250 264c40-10 52 30 50 60s40 40 100 14"/>
    </g>
    <g fill="none" stroke="#d8f04a" stroke-width="1.4">
      <path d="M338 70l16-6-4 16-4-6z"/>
      <path d="M30 180l16 12-16 2 4-6z"/>
      <path d="M244 258l-16 6 14 6-2-6z"/>
    </g>
  </svg>

  <div class="abs service-pill service-pill--blue" style="left:677px;top:89px">Next-Level Flyer</div>
  <p class="abs service-text" style="left:703px;top:128px;width:140px">Nicht nur Papier, sondern deine Botschaft im perfekten Look.</p>
  <div class="abs service-pill service-pill--cyan" style="left:677px;top:208px">Digital &amp; Print</div>
  <p class="abs service-text" style="left:703px;top:250px;width:140px">Ob Social Media Grafiken oder klassisches Printdesign – wir sind da, wo du uns brauchst.</p>

  <div class="abs service-pill service-pill--cyan" style="left:965px;top:124px">Corporate Identity</div>
  <p class="abs service-text" style="left:965px;top:166px;width:150px">Ein Design, das deine Marke spricht individuell, stark, unvergesslich.</p>
  <div class="abs service-pill service-pill--blue" style="left:965px;top:239px">Alles aus einer Hand</div>
  <p class="abs service-text" style="left:965px;top:281px;width:120px">Logo, Farben, Typografie, Flyer und vieles mehr – wir bauen das Fundament für deinen Erfolg</p>

  <div class="abs section-title" style="left:650px;top:384px">Warum wir?</div>
  <div class="abs why-row">
    <div class="why-card">
      <svg width="28" height="26" viewBox="0 0 28 26" aria-hidden="true"><rect x="3" y="4" width="20" height="14" rx="2" fill="none" stroke="#fff" stroke-width="2"/><path d="M9 22h8M13 18v4" stroke="#fff" stroke-width="2"/><path d="M12 14l10-10 3 3-10 10-4 1z" fill="#fff"/></svg>
      <strong>Dein Style, unser Know-how</strong>Wir kombinieren deine Vision mit moderner Ästhetik.
    </div>
    <div class="why-card why-card--mid">
      <svg width="28" height="26" viewBox="0 0 28 26" aria-hidden="true"><circle cx="14" cy="7" r="4" fill="#fff"/><path d="M6 22c0-5 4-8 8-8s8 3 8 8z" fill="#fff"/></svg>
      <strong>Persönlicher Service</strong>Wir hören zu und setzen um, was dich einzigartig macht
    </div>
    <div class="why-card">
      <svg width="28" height="26" viewBox="0 0 28 26" aria-hidden="true"><circle cx="14" cy="8" r="4" fill="#fff"/><path d="M7 22c0-4 3-7 7-7s7 3 7 7z" fill="#fff"/><path d="M4 6l4 2M24 6l-4 2M14 0v2" stroke="#fff" stroke-width="2"/></svg>
      <strong>Flexible Lösungen</strong>für die unterschiedlichsten Anforderungen
    </div>
  </div>
</section>

</body>
</html>
```